Transform Your Giving

I need a tri-fold brochure that will fit in a standard number 10 business envelope. Harborline and Steadfast Services is a charitable nonprofit. The goal of this brochure is to stimulate people into thinking about other ways to make a donation. The design should communicate the essential information on donation options, create a sense of professional integrity, be graphically sharp, easy to read and laid out in a way that doesn't make the material appear crowded.

```html
<!DOCTYPE html>
<html lang="en">
<head>
<meta charset="utf-8">
<title>Transform Your Giving – Harborline and Steadfast Services</title>
<link rel="stylesheet" href="https://fonts.googleapis.com/css2?family=Ubuntu:ital,wght@0,400;0,500;0,700;1,500;1,700&display=swap">
<style>
:root{
  --navy:#2a2775;
  --navy-deep:#231f66;
  --green:#3fb549;
  --ink:#2b2b2b;
  --backdrop:#7b7b7b;
  --white:#ffffff;
}
*{box-sizing:border-box;margin:0;padding:0}
html,body{width:1096px;height:1200px;overflow:hidden}
body{background:var(--backdrop);font-family:'Ubuntu',sans-serif;color:var(--ink);position:relative}
.sheet{position:absolute;left:205px;width:686px;height:515px;display:grid;grid-template-columns:repeat(3,1fr)}
.sheet--outside{top:63px}
.sheet--inside{top:621px}
.panel{position:relative;overflow:hidden;background:var(--white)}
.panel--navy{background:linear-gradient(170deg,#2f2b88 0%,#28246f 55%,#2a2775 100%);color:var(--white)}
.photo{position:absolute;left:0;width:100%}
.curve{position:absolute;left:0;width:100%;display:block}

/* icon grid */
.icon-set{position:absolute;left:0;width:100%}
.icon-row{display:flex;justify-content:center;align-items:flex-start}
.icon-item{display:flex;flex-direction:column;align-items:center;width:54px}
.icon-item .badge{width:42px;height:42px}
.icon-label{font-weight:700;font-size:10.4px;line-height:13px;color:var(--navy);text-align:center;margin-top:4px;white-space:nowrap}
.icon-link{width:26px;border-top:1.6px dotted var(--navy);margin-top:21px}

/* outside left */
.impact{position:absolute;left:18px;right:14px;top:230px}
.impact h2{font-size:12.2px;font-weight:700;color:var(--navy);letter-spacing:.1px}
.impact p{font-size:10.1px;line-height:13px;margin-top:2px;color:#222}

/* outside middle */
.contact-panel{text-align:center}
.lead{position:absolute;left:14px;right:14px;top:18px;font-size:8.8px;line-height:11.6px}
.quote{position:absolute;left:0;right:0;top:97px;font-size:8.8px;line-height:11.4px;font-weight:400;opacity:.95}
.will-note{position:absolute;left:0;right:0;top:201px;font-size:8.8px;line-height:11.4px}
.will-note a{color:var(--green)}
.mark{display:flex;align-items:center;justify-content:center;gap:6px;font-weight:700}
.mark--light{position:absolute;left:0;right:0;top:255px;font-size:38px;color:var(--white)}
.mark--dark{position:absolute;left:0;right:0;top:445px;font-size:44px;color:var(--navy)}
.mark-dot{display:inline-block;width:12px;height:12px;border-radius:50%;background:var(--green)}
.contact{position:absolute;left:0;right:0;top:329px}
.contact h3{font-size:10.5px;font-weight:700;text-decoration:underline;letter-spacing:.2px}
.contact .ask{font-size:8.8px;line-height:11.4px;font-weight:700;color:var(--green);margin-top:6px}
.contact-line{display:flex;flex-direction:column;align-items:center;font-size:8.6px;line-height:10.8px;margin-top:4px;letter-spacing:.2px}
.contact-line svg{width:9px;height:9px;margin-bottom:2px}
.follow{margin-top:10px;display:flex;align-items:center;justify-content:center;gap:3px;font-size:8.8px;font-weight:700}
.follow span.t{text-decoration:underline;margin-right:2px}
.social-dot{width:9px;height:9px;border-radius:50%;background:var(--green)}

/* outside right (cover) */
.cover-title{position:absolute;left:0;right:0;top:14px;text-align:center}
.cover-title h1{font-size:17.2px;line-height:20px;font-weight:700;color:var(--navy)}
.cover-title .accent{color:var(--green)}
.cover-title p{font-size:8.8px;line-height:11.4px;font-weight:700;color:var(--navy);margin-top:6px}

/* inside panels */
.inside{padding:19px 14px 0 18px}
.panel--navy.inside{padding:18px 14px 0 18px}
.intro{font-size:9.1px;line-height:11.5px;font-weight:500;color:#222}
.feature{display:flex;gap:6px;align-items:flex-start}
.feature .badge{flex:0 0 51px;width:51px;height:51px}
.feature h3{font-size:9.5px;line-height:11.6px;font-weight:700;color:var(--navy)}
.panel--navy .feature h3{color:var(--white);font-size:8.7px;line-height:11.2px}
.feature .tag{font-size:8.8px;line-height:11.3px;font-weight:700;font-style:italic;color:var(--green);margin-top:3px}
.body{font-size:8.5px;line-height:11px;color:#333}
.panel--navy .body{color:#eceaf7}
.how{font-size:10.6px;font-weight:700;color:var(--navy);margin-top:9px;line-height:12px}
.panel--navy .how{color:var(--green)}
.checks{list-style:none;margin-top:8px}
.checks li{position:relative;padding-left:10px;font-size:7.9px;line-height:10.2px;color:#333;margin-bottom:6px}
.checks li svg{position:absolute;left:0;top:2px;width:7px;height:7px}
</style>
</head>
<body>

<svg width="0" height="0" style="position:absolute" aria-hidden="true">
  <defs>
    <symbol id="glyph-coin" viewBox="0 0 24 24"><g fill="none" stroke="#fff" stroke-width="1.4" stroke-linecap="round"><circle cx="12" cy="12" r="7"/><circle cx="12" cy="12" r="4.5"/><path d="M10 12h4"/></g></symbol>
    <symbol id="glyph-bank" viewBox="0 0 24 24"><g fill="none" stroke="#fff" stroke-width="1.3" stroke-linejoin="round"><path d="M4 9 12 4.5 20 9Z"/><path d="M5 10.5h14M5 18h14M4 19.8h16"/><path d="M7 11v6M10 11v6M14 11v6M17 11v6"/></g></symbol>
    <symbol id="glyph-gift" viewBox="0 0 24 24"><g fill="none" stroke="#fff" stroke-width="1.3" stroke-linejoin="round"><rect x="5" y="10.5" width="14" height="8.5"/><rect x="4" y="7.5" width="16" height="3"/><path d="M12 7.5V19"/><path d="M12 7.5C10 4 7 5 8.5 7.5M12 7.5c2-3.5 5-2.5 3.5 0"/></g></symbol>
    <symbol id="glyph-chart" viewBox="0 0 24 24"><g fill="none" stroke="#fff" stroke-width="1.3" stroke-linejoin="round"><rect x="5" y="14" width="3" height="5"/><rect x="10" y="11" width="3" height="8"/><rect x="15" y="8.5" width="3" height="10.5"/><path d="M4 12 9 8 12 10 19 5"/><path d="M16 5h3v3"/><path d="M3.5 19.5h17"/></g></symbol>
    <symbol id="glyph-calendar" viewBox="0 0 24 24"><g fill="none" stroke="#fff" stroke-width="1.2"><rect x="4.5" y="6" width="15" height="13" rx="1"/><path d="M4.5 9.5h15M8 4.5v3M16 4.5v3"/><circle cx="12" cy="9" r="2.6" fill="#fff" fill-opacity=".15"/><path d="M7 13h2M11 13h2M15 13h2M7 16h2M11 16h2M15 16h2"/></g></symbol>
  </defs>
</svg>

<!-- OUTSIDE SHEET -->
<section class="sheet sheet--outside">

  <article class="panel">
    <div class="photo" style="top:0;height:232px;background:linear-gradient(160deg,#e9e6e2 0%,#cfc4b8 45%,#9a8878 100%)" role="img" aria-label="Photo of a young woman helping an older man use a tablet at home"></div>
    <svg class="curve" style="top:206px" viewBox="0 0 229 30" height="30" preserveAspectRatio="none" aria-hidden="true">
      <path d="M0 30 Q114 -8 229 30 Z" fill="#fff"/>
      <path d="M0 30 Q114 -8 229 30" fill="none" stroke="var(--green)" stroke-width="3"/>
    </svg>
    <div class="impact">
      <h2>THE IMPACT OF YOUR GIFT</h2>
      <p>Your generosity drives our mission. With every Smart gift you’re supporting Harborline and Steadfast Services. Join our community of Smart Givers today and make an enduring impact. With Smart Giving your generosity reaches further.&nbsp; Begin your Smart Giving journey with us today.</p>
    </div>
    <div class="icon-set" style="top:367px">
      <div class="icon-row">
        <div class="icon-item"><svg class="badge" viewBox="0 0 42 42"><circle cx="21" cy="21" r="20" fill="var(--navy)"/><circle cx="21" cy="21" r="17.5" fill="none" stroke="#fff" stroke-width="1"/><use href="#glyph-coin" x="8" y="8" width="26" height="26"/></svg><span class="icon-label">CRYPTO</span></div>
        <div class="icon-link"></div>
        <div class="icon-item"><svg class="badge" viewBox="0 0 42 42"><circle cx="21" cy="21" r="20" fill="var(--navy)"/><circle cx="21" cy="21" r="17.5" fill="none" stroke="#fff" stroke-width="1"/><use href="#glyph-bank" x="8" y="8" width="26" height="26"/></svg><span class="icon-label">DAF’S</span></div>
        <div class="icon-link"></div>
        <div class="icon-item"><svg class="badge" viewBox="0 0 42 42"><circle cx="21" cy="21" r="20" fill="var(--navy)"/><circle cx="21" cy="21" r="17.5" fill="none" stroke="#fff" stroke-width="1"/><use href="#glyph-gift" x="8" y="8" width="26" height="26"/></svg><span class="icon-label">QCDS</span></div>
      </div>
      <div class="icon-row" style="margin-top:4px">
        <div class="icon-item" style="width:66px"><svg class="badge" viewBox="0 0 42 42"><circle cx="21" cy="21" r="20" fill="var(--navy)"/><circle cx="21" cy="21" r="17.5" fill="none" stroke="#fff" stroke-width="1"/><use href="#glyph-chart" x="8" y="8" width="26" height="26"/></svg><span class="icon-label">STOCKS &amp;<br>SECURITIES</span></div>
        <div class="icon-link" style="margin-left:-6px;margin-right:-6px"></div>
        <div class="icon-item" style="width:66px"><svg class="badge" viewBox="0 0 42 42"><circle cx="21" cy="21" r="20" fill="var(--navy)"/><circle cx="21" cy="21" r="17.5" fill="none" stroke="#fff" stroke-width="1"/><use href="#glyph-calendar" x="8" y="8" width="26" height="26"/></svg><span class="icon-label">CHARITABLE<br>ANNUITY</span></div>
      </div>
    </div>
  </article>

  <article class="panel panel--navy contact-panel">
    <p class="lead">To learn more about Smart Giving Options and how they can benefit you and Harborline and Steadfast Services, please reach out to our team.&nbsp; We’re here to help you navigate these giving methods and answer any question you may have.</p>
    <p class="quote">Being kind to others is a way of<br>being good to yourself.<br>Miriam Albright</p>
    <p class="will-note">If you do not have a will, go to<br><a href="#">www.OpenWillForm.com.</a><br>In 20 minutes you can have a legal will – for free.</p>
    <div class="mark mark--light"><span class="mark-dot"></span>HSS</div>
    <div class="contact">
      <h3>CONTACT US</h3>
      <p class="ask">Have more question? Please contact us at<br>Harborline and Steadfast Services</p>
      <div class="contact-line"><svg viewBox="0 0 10 10"><circle cx="5" cy="5" r="5" fill="var(--green)"/><path d="M5 2.2a1.8 1.8 0 0 1 1.8 1.8C6.8 5.4 5 7.6 5 7.6S3.2 5.4 3.2 4A1.8 1.8 0 0 1 5 2.2Z" fill="#fff"/></svg>2150 Alder Row<br>Suite 4 Fairhaven, ND&nbsp; 58512</div>
      <div class="contact-line"><svg viewBox="0 0 10 10"><circle cx="5" cy="5" r="5" fill="var(--green)"/><path d="M3.3 2.6c.4-.3.8 0 1 .5l.2.6-.5.5c.3.7.8 1.2 1.5 1.5l.5-.5.6.2c.5.2.8.6.5 1-.7 1-3.6-.6-4.2-3.2Z" fill="#fff"/></svg>701-555-0148 (ext. 100)</div>
      <div class="contact-line"><svg viewBox="0 0 10 10"><circle cx="5" cy="5" r="5" fill="var(--green)"/><rect x="2.6" y="3.2" width="4.8" height="3.6" fill="#fff"/><path d="M2.6 3.3 5 5.2 7.4 3.3" fill="none" stroke="var(--green)" stroke-width=".6"/></svg>tmarlow@harborlinehss.org</div>
      <div class="contact-line"><svg viewBox="0 0 10 10"><circle cx="5" cy="5" r="5" fill="var(--green)"/><circle cx="5" cy="5" r="2.6" fill="none" stroke="#fff" stroke-width=".7"/><path d="M2.4 5h5.2M5 2.4c-1.2 1.5-1.2 3.7 0 5.2M5 2.4c1.2 1.5 1.2 3.7 0 5.2" fill="none" stroke="#fff" stroke-width=".5"/></svg>www.harborlinehss.org</div>
      <div class="follow"><span class="t">FOLLOW US:</span><span class="social-dot"></span><span class="social-dot"></span></div>
    </div>
  </article>

  <article class="panel">
    <header class="cover-title">
      <h1>Transform Your Giving<br><span class="accent">Be Strategic, Be Smart</span></h1>
      <p>Discover the impact of Smart Giving with<br>Harborline and Steadfast Services</p>
    </header>
    <svg class="curve" style="top:85px" viewBox="0 0 229 30" height="30" preserveAspectRatio="none" aria-hidden="true">
      <path d="M0 28 Q114 -6 229 28" fill="none" stroke="var(--green)" stroke-width="3"/>
    </svg>
    <div class="photo" style="top:94px;height:200px;background:linear-gradient(150deg,#7b9a3a 0%,#a7b86a 35%,#d7c6b2 60%,#8fb2c8 100%);clip-path:path('M0 30 Q114 -4 229 30 L229 200 L0 200 Z')" role="img" aria-label="Photo of a smiling older couple embracing outdoors"></div>
    <svg class="curve" style="top:264px" viewBox="0 0 229 32" height="32" preserveAspectRatio="none" aria-hidden="true">
      <path d="M0 32 Q114 -6 229 32 Z" fill="#fff"/>
      <path d="M0 32 Q114 -6 229 32" fill="none" stroke="var(--green)" stroke-width="3"/>
    </svg>
    <div class="icon-set" style="top:289px">
      <div class="icon-row">
        <div class="icon-item"><svg class="badge" viewBox="0 0 42 42"><circle cx="21" cy="21" r="20" fill="var(--navy)"/><circle cx="21" cy="21" r="17.5" fill="none" stroke="#fff" stroke-width="1"/><use href="#glyph-coin" x="8" y="8" width="26" height="26"/></svg><span class="icon-label">CRYPTO</span></div>
        <div class="icon-link"></div>
        <div class="icon-item"><svg class="badge" viewBox="0 0 42 42"><circle cx="21" cy="21" r="20" fill="var(--navy)"/><circle cx="21" cy="21" r="17.5" fill="none" stroke="#fff" stroke-width="1"/><use href="#glyph-bank" x="8" y="8" width="26" height="26"/></svg><span class="icon-label">DAF’S</span></div>
        <div class="icon-link"></div>
        <div class="icon-item"><svg class="badge" viewBox="0 0 42 42"><circle cx="21" cy="21" r="20" fill="var(--navy)"/><circle cx="21" cy="21" r="17.5" fill="none" stroke="#fff" stroke-width="1"/><use href="#glyph-gift" x="8" y="8" width="26" height="26"/></svg><span class="icon-label">QCDS</span></div>
      </div>
      <div class="icon-row" style="margin-top:2px">
        <div class="icon-item" style="width:66px"><svg class="badge" viewBox="0 0 42 42"><circle cx="21" cy="21" r="20" fill="var(--navy)"/><circle cx="21" cy="21" r="17.5" fill="none" stroke="#fff" stroke-width="1"/><use href="#glyph-chart" x="8" y="8" width="26" height="26"/></svg><span class="icon-label">STOCKS &amp;<br>SECURITIES</span></div>
        <div class="icon-link" style="margin-left:-6px;margin-right:-6px"></div>
        <div class="icon-item" style="width:66px"><svg class="badge" viewBox="0 0 42 42"><circle cx="21" cy="21" r="20" fill="var(--navy)"/><circle cx="21" cy="21" r="17.5" fill="none" stroke="#fff" stroke-width="1"/><use href="#glyph-calendar" x="8" y="8" width="26" height="26"/></svg><span class="icon-label">CHARITABLE<br>ANNUITY</span></div>
      </div>
    </div>
    <div class="mark mark--dark"><span class="mark-dot"></span>HSS</div>
  </article>
</section>

<!-- INSIDE SHEET -->
<section class="sheet sheet--inside">

  <article class="panel inside">
    <p class="intro">We would like to introduce you to five Strategic and Smart ways to give that could potentially be more beneficial to you compared to traditional cash donations. We encourage you to keep this information as a guide for your future contributions.</p>

    <div class="feature" style="margin-top:8px">
      <svg class="badge" viewBox="0 0 52 52"><circle cx="26" cy="26" r="24.5" fill="#fff" stroke="var(--green)" stroke-width="2.6"/><circle cx="26" cy="26" r="20.5" fill="var(--navy)"/><use href="#glyph-chart" x="11" y="11" width="30" height="30"/></svg>
      <div>
        <h3>Gifts of Stocks or Appreciated Assets Strategic &amp; Smart</h3>
        <p class="tag">Consider your long-term publicly traded stock as a way to give to your favorite charity.</p>
      </div>
    </div>
    <p class="body" style="margin-top:3px">You can make a significantly bigger impact when you donate long-term appreciated securities, including stock, mutual funds, &amp; bonds, directly to your favorite charity.</p>
    <h4 class="how">How Does It Work?</h4>
    <p class="body">When you donate stock to a charity, you will generally take a tax deduction for the full market value. Because you are donating stock, your contribution &amp; tax deduction may be significantly higher than contributing the after-tax proceeds. The same benefits apply when you donate mutual funds or bonds.</p>

    <div class="feature" style="margin-top:14px">
      <svg class="badge" viewBox="0 0 52 52"><circle cx="26" cy="26" r="24.5" fill="#fff" stroke="var(--green)" stroke-width="2.6"/><circle cx="26" cy="26" r="20.5" fill="var(--navy)"/><use href="#glyph-bank" x="11" y="11" width="30" height="30"/></svg>
      <div>
        <h3>Donor-Advised Fund (DAF)<br>Strategic &amp; Smart</h3>
        <p class="tag">Consider a DAF – a simple, flexible, and tax-advantageous way to give to your favorite charities.</p>
      </div>
    </div>
    <p class="body" style="margin-top:3px">A Donor-Advised Fund (DAF), is like a charitable investment account for the sole purpose of supporting your favorite charities.</p>
    <h4 class="how">How Does It Work?</h4>
    <p class="body" style="font-size:7.9px;line-height:10.4px">You establish a DAF &amp; contribute cash, stocks, or non-publicly traded assets, cryptocurrency, &amp; private company stock to be eligible for an immediate tax deduction. Those funds are contributed for tax-free growth. You can recommend grants be made from your DAF to any IRS qualified public charity.</p>
  </article>

  <article class="panel panel--navy inside">
    <div class="feature">
      <svg class="badge" viewBox="0 0 52 52"><circle cx="26" cy="26" r="25" fill="var(--green)"/><circle cx="26" cy="26" r="21" fill="none" stroke="#fff" stroke-width="1.4"/><use href="#glyph-gift" x="11" y="11" width="30" height="30"/></svg>
      <div>
        <h3>Qualified Charitable Distributions (QCDs) Strategic &amp; Smart</h3>
        <p class="tag" style="font-size:8.4px;line-height:11px">Consider a QCD – when planning your IRA withdrawal strategy... &amp; donate to your favorite charity.</p>
      </div>
    </div>
    <p class="body" style="margin-top:3px">IRA owners at age 70 ½ or over can transfer dollars from their IRA to charity tax-free each year. These transfers known as Qualified Charitable Distributions (QCDs) offer eligible older Americans a great way to easily give to charity.</p>
    <h4 class="how">How Does It Work?</h4>
    <p class="body">Are you 72 and required to take a minimum distribution (RMD) from your IRA but do not need the funds? Consider a Qualified Charitable Distribution. Normally, distributions from a traditional IRA are taxable when received. With a QCD, these distributions become tax-free when paid directly from the IRA to your favorite eligible charity. An IRA owner wishing to make a QCD should contact their IRA trustee, allowing time to complete the transaction before the end of the year to receive the tax benefit.</p>

    <div class="feature" style="margin-top:18px">
      <svg class="badge" viewBox="0 0 52 52"><circle cx="26" cy="26" r="25" fill="var(--green)"/><circle cx="26" cy="26" r="21" fill="none" stroke="#fff" stroke-width="1.4"/><use href="#glyph-calendar" x="11" y="11" width="30" height="30"/></svg>
      <div>
        <h3>Charitable Gift Annuity<br>Strategic &amp; Smart</h3>
        <p class="tag" style="font-size:8.4px;line-height:11px">Consider establishing a<br>Charitable Gift Annuity</p>
      </div>
    </div>
    <p class="body" style="margin-top:5px">You make a donation to a single charity. The gift is set aside in a reserve account and invested.</p>
    <h4 class="how" style="margin-top:7px">How Does It Work?</h4>
    <p class="body">A charitable gift annuity is a contract between a donor &amp; a charity. As a donor, you make a sizable gift to charity using cash, securities, or possibly other assets. This money is then invested. In return, you become eligible to take a partial tax deduction for your donation, plus you receive a fixed stream of income from the charity for the rest of your life. At the end of your life (as well as your spouse’s, if you’re giving as a couple), the charity receives the remainder of the gift.</p>
  </article>

  <article class="panel inside">
    <div class="feature">
      <svg class="badge" viewBox="0 0 52 52"><circle cx="26" cy="26" r="24.5" fill="#fff" stroke="var(--green)" stroke-width="2.6"/><circle cx="26" cy="26" r="20.5" fill="var(--navy)"/><use href="#glyph-coin" x="11" y="11" width="30" height="30"/></svg>
      <div>
        <h3 style="font-size:10.4px;line-height:13px">Cryptocurrency<br>Strategic &amp; Smart</h3>
        <p class="tag">Consider donating Bitcoin and other cryptocurrencies to your favorite charity.</p>
      </div>
    </div>
    <p class="body" style="margin-top:8px;font-size:9.1px;line-height:11.9px">Bitcoin and other cryptocurrencies can be donated to charity just like other appreciated assets such as stocks and other business interests. Before you sell bitcoin &amp; donate the after-tax proceeds, consider donating your bitcoin directly to a favorite charity.</p>
    <h4 class="how" style="margin-top:12px">How Does It Work?</h4>
    <p class="body">Many donors find it useful to open a Donor-Advised Fund (DAF). This strategy includes two significant benefits, both for you and your favorite charity.</p>
    <ul class="checks">
      <li><svg viewBox="0 0 10 10"><circle cx="5" cy="5" r="5" fill="var(--navy)"/><path d="M2.8 5.2 4.4 6.7 7.2 3.6" fill="none" stroke="#fff" stroke-width="1.2"/></svg>Your tax deduction will be equal to the fair market value of the donated bitcoin (as determined by a qualified appraisal).</li>
      <li><svg viewBox="0 0 10 10"><circle cx="5" cy="5" r="5" fill="var(--navy)"/><path d="M2.8 5.2 4.4 6.7 7.2 3.6" fill="none" stroke="#fff" stroke-width="1.2"/></svg>Your cryptocurrency donation is tax-smart because it may eliminate capital gains taxes on the value / appreciation AND your favorite charity will receive 100% of the value of the contribution.</li>
    </ul>
    <p class="body">Often charities are not able to accept direct donations of bitcoin/crypto so using a DAF is a great way to donate these assets.</p>

    <div class="photo" style="top:367px;height:148px;background:linear-gradient(160deg,#5f8a3c 0%,#90a870 40%,#b8a894 70%,#6e7f5a 100%)" role="img" aria-label="Photo of an older couple sitting on a park bench with shopping bags"></div>
    <svg class="curve" style="top:358px" viewBox="0 0 229 30" height="30" preserveAspectRatio="none" aria-hidden="true">
      <path d="M0 30 L0 0 L229 0 L229 30 Q114 -4 0 30 Z" fill="#fff"/>
      <path d="M0 26 Q114 -8 229 26" fill="none" stroke="var(--green)" stroke-width="3"/>
    </svg>
  </article>
</section>

</body>
</html>
```